Web Pages Improvement, Update of existing MIRB website

Redesign existing website www.mirb.asn.au The # of pages can be reduced to a total of 6 including the home page. We have a design project out for the logo for this site so feel free to bid for that also.
As this is a simple brief with basic pages, we expect the end result to be code ready for uploaded to our existing host.

```html
<!DOCTYPE html>
<html lang="en">
<head>
<meta charset="utf-8">
<title>MIRB – Measurement Inspection Review Board</title>
<link rel="stylesheet" href="https://fonts.googleapis.com/css2?family=Ubuntu:wght@400;500;700&display=swap">
<style>
  :root {
    --brand-orange: #f7a035;
    --band-top: #ff8b45;
    --band-bottom: #fdca7b;
    --card-top: #ffffff;
    --card-bottom: #e9e9e9;
    --ink: #1e1e1e;
    --rule: #d4d4d4;
    --header-bg: #fbfbfb;
    --footer-bg: #efefef;
  }
  * { box-sizing: border-box; margin: 0; padding: 0; }
  html, body { width: 1200px; height: 1182px; overflow: hidden; }
  body {
    font-family: "Ubuntu", Arial, sans-serif;
    color: var(--ink);
    background: var(--header-bg);
    position: relative;
  }
  .site-header {
    position: absolute; left: 0; top: 0; width: 1200px; height: 119px;
    background: linear-gradient(#ffffff, #f2f2f2);
    box-shadow: 0 4px 8px rgba(120, 60, 0, .35);
    z-index: 2;
  }
  .brand {
    position: absolute; left: 89px; top: 12px;
    font-family: Arial, Helvetica, sans-serif;
    font-size: 70px; font-weight: 400; color: var(--brand-orange);
    letter-spacing: 1px; line-height: 1;
  }
  .brand-tagline {
    position: absolute; left: 37px; top: 93px;
    font-family: Arial, Helvetica, sans-serif;
    font-size: 14px; color: var(--brand-orange); word-spacing: 6px;
  }
  .main-nav { position: absolute; right: 70px; top: 40px; display: flex; gap: 24px; }
  .main-nav a {
    font-family: Arial, Helvetica, sans-serif;
    font-size: 27px; color: var(--brand-orange); text-decoration: none;
  }
  .page-band {
    position: absolute; left: 0; top: 119px; width: 1200px; height: 1015px;
    background: linear-gradient(var(--band-top), var(--band-bottom));
  }
  .content-card {
    position: absolute; left: 17px; top: 25px; width: 1168px; height: 942px;
    background: linear-gradient(var(--card-top), var(--card-bottom));
    border-radius: 6px;
  }
  .column { position: absolute; top: 0; }
  .column-left { left: 41px; width: 480px; }
  .column-right { left: 643px; width: 484px; }
  .divider {
    position: absolute; left: 586px; top: 82px; width: 1px; height: 823px;
    background: var(--rule);
  }
  h2 { font-size: 25px; font-weight: 700; position: absolute; top: 25px; left: 6px; white-space: nowrap; }
  h3 { font-size: 17px; font-weight: 700; margin-bottom: 11px; }
  .column-body { position: absolute; top: 78px; left: 0; width: 100%; }
  p { font-size: 17.3px; line-height: 19.7px; text-indent: 42px; margin-bottom: 7px; }
  .purpose-list { list-style: none; counter-reset: item; margin: 4px 0 22px; }
  .purpose-list li {
    counter-increment: item; position: relative;
    font-size: 15.5px; line-height: 17.9px; padding-left: 42px; text-indent: -12px;
    margin-bottom: 8px; width: 418px;
  }
  .purpose-list li::before {
    content: counter(item) "."; position: absolute; left: 3px; text-indent: 0;
  }
  .mark-row {
    position: absolute; left: 57px; top: 780px; width: 380px; height: 60px;
  }
  .site-footer {
    position: absolute; left: 0; top: 1134px; width: 1200px; height: 48px;
    background: linear-gradient(#f7f7f7, var(--footer-bg));
    display: flex; align-items: center; justify-content: space-between;
    padding: 0 15px 0 36px; font-size: 18px;
  }
  .footer-nav { display: flex; gap: 24px; }
  .footer-nav a { color: var(--ink); text-decoration: none; }
</style>
</head>
<body>
  <header class="site-header">
    <div class="brand">MIRB</div>
    <div class="brand-tagline">Measurement Inspection Review Board</div>
    <nav class="main-nav">
      <a href="#">Home</a><a href="#">Members</a><a href="#">Contact</a>
    </nav>
  </header>

  <div class="page-band">
    <main class="content-card">
      <section class="column column-left">
        <h2>Overview</h2>
        <div class="column-body">
          <h3>Measurement Inspection Review Board</h3>
          <p>The Measurement Inspection Review Board of Australia (MIRB) was established in 1995 to foster the growth of a professional and value adding compliance testing resource to serve the needs of Australian industry.</p>
          <p>MIRB is an incorporated association formed by NLAB accredited electrical testing laboratories in Australia and includes an accredited member from New Zealand. The association has 14 active members which operate laboratories in a total of 18 locations in Australia and New Zealand. The members provide testing services to the public in the areas of electrical safety, electromagnetic compatibility, electromagnetic radiation, electromedical equipment, energy efficiency labelling, environmental performance, gas appliances, lighting equipment, performance ratings, and telecommunications. The NLAB accreditation mark is shown below.</p>
          <p>The Association operates a paid secretariat to service the interests of its members and to provide information about the services available to the public from its members. The registered office is in Elmwood, Victoria. The members of MIRB meet regularly to discuss issues of interest to its members and the testing industry and to make submissions to regulators, public investigations, inquiries and industry surveys. The Association nominates members to serve on relevant Committees of the Standards Council and to make representations to government inquiries.</p>
          <p>Member laboratories of MIRB test equipment to Australian and International Standards so that the clients are able to apply the appropriate regulatory mark for their product. The commonly recognised regulatory marks are the K-Mark and R-Mark for Australia, EQ for Europe, UCL for the USA as shown below.</p>
        </div>
        <svg class="mark-row" viewBox="0 0 380 60" role="img" aria-label="Accreditation and regulatory marks">
          <rect x="0" y="10" width="34" height="34" fill="#111" transform="rotate(45 17 27)"/>
          <circle cx="105" cy="27" r="22" fill="#111"/>
          <rect x="172" y="6" width="44" height="44" rx="6" fill="#111"/>
          <circle cx="286" cy="27" r="22" fill="#111"/>
          <rect x="330" y="7" width="50" height="40" fill="#111"/>
        </svg>
      </section>

      <div class="divider"></div>

      <section class="column column-right">
        <h2>Our services</h2>
        <div class="column-body">
          <h3>Statement of purpose</h3>
          <p>The Measurement Inspection Review Board of Australia has been established is to foster the growth of a professional and value adding compliance testing resource to serve the needs of Australian Industry.</p>
          <p>The Association may involve itself in such activities as are consistent with the above stated object of the Association and which the Committee has approved including:</p>
          <ol class="purpose-list">
            <li>Sharing of information through activities such as interpretation working groups and internal and external education.</li>
            <li>Promotion of the value of testing results obtained from appropriately accredited test houses.</li>
            <li>Participation in standards writing committees and working groups.</li>
            <li>Provision of advice to Government on policy issues.</li>
            <li>Provision of advice to Industry on compliance and approval issues.</li>
            <li>Enhancement of the international competitiveness of Australian Industry by promoting compliance with internationally harmonised standards.</li>
            <li>Promotion of the professional development of the membership.</li>
            <li>Development and enforcement of a Code of Ethics.</li>
            <li>Such activities as approved by the committee and which are of benefit to the industry.</li>
          </ol>
          <h3>Types of Testing</h3>
          <p>The member laboratories of MIRB provide a wide range of accredited testing services, with the main activities being in the electrical safety, electromagnetic compatibility and telecommunications areas. With the trend to harmonized standards internationally the NLAB accredited testing services are recognized and accepted overseas.</p>
          <p>The member listing on the following pages detail the accreditations held by the laboratories and perusal of these is a sound starting point to determining which laboratory to approach.</p>
        </div>
      </section>
    </main>
  </div>

  <footer class="site-footer">
    <nav class="footer-nav">
      <a href="#">Home</a><a href="#">Members</a><a href="#">Contact</a>
    </nav>
    <span>Copyright © MIRB</span>
  </footer>
</body>
</html>
```